Graphics for Corvella telehealth weight loss plans

Corvella focuses on delivering medical weight-loss using prescription medicine and telehealth consults. Corvella needs graphics for its ecommerce site for three weight loss plans. The plans are posted here with current graphics and descriptions of what is included with each plan. Please do not feel constrained by current graphics or styling.

- https://store.corvellacare.com/products/radiant-horizon-plan
- https://store.corvellacare.com/products/brightpath-core-plan
- https://store.corvellacare.com/products/daily-harbor-plan

The graphics need to look good on mobile and desktop browsers.

```html
<!DOCTYPE html>
<html lang="en">
<head>
<meta charset="utf-8">
<title>Daily Harbor Plan – Corvella</title>
<link rel="stylesheet" href="https://fonts.googleapis.com/css2?family=Fira+Sans:wght@400;800&family=Fira+Sans+Condensed:wght@800&display=swap">
<style>
  :root {
    --backdrop: #9a9da4;
    --navy: #3e5680;
    --photo-light: #b9c9ea;
    --photo-mid: #7f95c2;
    --pill: #c07c74;
    --white: #ffffff;
  }
  * { margin: 0; padding: 0; box-sizing: border-box; }
  html, body {
    width: 1200px; height: 1200px; overflow: hidden;
    background: var(--backdrop);
  }
  .plan-card {
    position: absolute;
    left: 177px; top: 53px;
    width: 846px; height: 1094px;
    background: var(--navy);
    overflow: hidden;
  }
  .plan-title {
    position: absolute;
    top: 58px; left: 0; width: 100%;
    text-align: center;
    font-family: "Fira Sans", sans-serif;
    font-weight: 800;
    font-size: 70px;
    letter-spacing: -1px;
    color: var(--white);
    line-height: 1;
  }
  .hero-photo {
    position: absolute;
    left: 0; top: 161px;
    width: 100%; height: 528px;
    background:
      linear-gradient(to bottom, rgba(62,86,128,0.6) 0%, rgba(62,86,128,0) 8%, rgba(62,86,128,0) 78%, var(--navy) 100%),
      radial-gradient(ellipse at 60% 45%, var(--photo-light) 0%, var(--photo-mid) 65%, #5d74a3 100%);
  }
  .includes-tag {
    position: absolute;
    left: 57px; top: 624px;
    width: 239px; height: 65px;
    border-radius: 18px;
    background: var(--pill);
    color: var(--white);
    font-family: "Fira Sans Condensed", sans-serif;
    font-weight: 800;
    font-size: 38px;
    line-height: 65px;
    padding-left: 34px;
  }
  .benefit-list {
    position: absolute;
    left: 66px; top: 738px;
    width: 560px;
    list-style: none;
    font-family: "Fira Sans", sans-serif;
    font-weight: 400;
    font-size: 30px;
    line-height: 37px;
    letter-spacing: 0.5px;
    color: var(--white);
  }
  .benefit-list li {
    position: relative;
    display: flex;
    align-items: center;
    padding-left: 56px;
    margin-bottom: 23px;
  }
  .benefit-list li:first-child { padding-left: 54px; }
  .benefit-list svg {
    position: absolute;
    left: 0; top: 50%;
    transform: translateY(-50%);
  }
</style>
</head>
<body>
  <article class="plan-card">
    <h1 class="plan-title">Daily Harbor Plan</h1>
    <div class="hero-photo" role="img" aria-label="Smiling woman in glasses and a white T-shirt reading a tablet at a kitchen counter beside fresh fruit, toned in blue"></div>
    <div class="includes-tag">Includes</div>
    <ul class="benefit-list">
      <li><svg width="12" height="14" viewBox="0 0 12 14" aria-hidden="true"><path d="M0 0 L12 7 L0 14 Z" fill="#fff"/></svg>Expert Nutrition Consult</li>
      <li><svg width="12" height="14" viewBox="0 0 12 14" aria-hidden="true"><path d="M0 0 L12 7 L0 14 Z" fill="#fff"/></svg>Customer Crafted Diet Plan to achieve your goals</li>
      <li><svg width="12" height="14" viewBox="0 0 12 14" aria-hidden="true"><path d="M0 0 L12 7 L0 14 Z" fill="#fff"/></svg>Nutritionist coaching to improve your health and vitality</li>
      <li><svg width="12" height="14" viewBox="0 0 12 14" aria-hidden="true"><path d="M0 0 L12 7 L0 14 Z" fill="#fff"/></svg>Month to month pay as you go</li>
    </ul>
  </article>
</body>
</html>
```